" A KRV tecnologia irá atuar em desenvolvimento de software e soluçoes em infraestrutura de informática com enfoque em soluçao de software livre (opensource) como freebsd e linux. A empresa trabalhará com desenvolvimento de softwares próprios para comércio de licenças, software sob demanda para terceiros, consultoria em servidores de alta disponibilidade, linux, freebsd, e rede em geral. Enfoque em soluçoes web, tanto no desenvolvimento quanto na infraestrutura. "

```html
<!DOCTYPE html>
<html lang="pt-BR">
<head>
<meta charset="UTF-8">
<title>KRV tecnologia — cartão de visita</title>
<link href="https://fonts.googleapis.com/css2?family=Open+Sans:wght@400;600;800&display=swap" rel="stylesheet">
<style>
  :root {
    --brand-blue: #2f80c8;
    --brand-orange: #f05a28;
    --paper: #ffffff;
    --backdrop: #e6e7e9;
    --muted-blue: #8fa9c4;
  }
  * { margin: 0; padding: 0; box-sizing: border-box; }
  html, body { width: 1200px; height: 1200px; overflow: hidden; }
  body {
    background: var(--backdrop);
    font-family: "Open Sans", Arial, sans-serif;
    display: flex;
    flex-direction: column;
    align-items: center;
    justify-content: center;
    gap: 60px;
  }
  .card {
    position: relative;
    width: 880px;
    height: 490px;
    overflow: hidden;
    box-shadow: 0 10px 30px rgba(0,0,0,0.18);
  }
  /* Verso azul */
  .card--back { background: var(--brand-blue); color: var(--paper); }
  .brand {
    position: absolute;
    display: flex;
    align-items: center;
    gap: 14px;
  }
  .brand__dot {
    width: 46px; height: 46px;
    border-radius: 50%;
    background: var(--brand-orange);
  }
  .brand__text { display: flex; flex-direction: column; line-height: 1; }
  .brand__name { font-weight: 800; font-size: 64px; letter-spacing: 1px; }
  .brand__tag {
    font-weight: 600; font-size: 13px; letter-spacing: 3px;
    text-transform: uppercase; margin-top: 4px; align-self: flex-end;
  }
  .card--back .brand { right: 250px; top: 90px; }
  .card--back .brand__name, .card--back .brand__tag { color: var(--paper); }

  .contact {
    position: absolute;
    left: 70px; bottom: 70px;
    font-size: 20px;
    line-height: 1.35;
  }
  .contact__name { font-size: 24px; font-weight: 400; letter-spacing: 1px; }
  .contact__role { margin-bottom: 18px; }
  .contact__block { margin-top: 14px; font-size: 18px; }

  /* Frente */
  .card--front { background: var(--brand-blue); }
  .card--front svg.panels { position: absolute; inset: 0; }
  .card--front .brand { right: 110px; bottom: 120px; }
  .card--front .brand__name { color: var(--brand-blue); }
  .card--front .brand__tag { color: var(--muted-blue); }
  .web {
    position: absolute;
    left: 50px; bottom: 45px;
    color: var(--paper);
    font-size: 22px;
  }
  .web strong { font-weight: 800; }
</style>
</head>
<body>

  <section class="card card--back" aria-label="Verso do cartão">
    <div class="brand">
      <span class="brand__dot"></span>
      <div class="brand__text">
        <span class="brand__name">KRV</span>
        <span class="brand__tag">tecnologia</span>
      </div>
    </div>
    <div class="contact">
      <p class="contact__name">MARCOS RIBEIRO</p>
      <p class="contact__role">Gerente Geral</p>
      <p>(16) 33452190</p>
      <p>(16) 99812374</p>
      <div class="contact__block">
        <p>contato@krvtec.com.br</p>
        <p>Rua das Palmeiras, nº 412, Centro</p>
        <p>CEP: 14020-310</p>
      </div>
    </div>
  </section>

  <section class="card card--front" aria-label="Frente do cartão">
    <svg class="panels" width="880" height="490" viewBox="0 0 880 490" aria-hidden="true">
      <rect x="0" y="0" width="800" height="490" fill="var(--paper)"/>
      <polygon points="0,0 800,0 380,490 0,490" fill="var(--brand-orange)"/>
    </svg>
    <div class="brand">
      <span class="brand__dot"></span>
      <div class="brand__text">
        <span class="brand__name">KRV</span>
        <span class="brand__tag">tecnologia</span>
      </div>
    </div>
    <p class="web">www.<strong>krv</strong>.com.br</p>
  </section>

</body>
</html>
```